TitleForge.com - Brandable Business Name Marketplace!

What is Title Forge?
Title Forge is a website that helps businesses build a name (or find a new name) for
their new product, service, or business. Over 2 million new businesses start each year,
and even more new products are created, and each one needs a unique name!
Other competitor branding sites for reference: www.MarkPail.com, www.Titlestic.com, www.MarkStem.com, www.markzo.com
What does Title Forge do?
Every business/product has a website, and the ‘address’ of the website is called
a ‘domain name’. We find valuable ‘domain names’ that are unique, catchy, or keyword-rich.
We then create a logo to capture the vision of the possibilities of that name. Then we write a
creative description of name, which further evolves the vision of the name.
We also help domain owners submit and sell their valuable digital real estate (domain).
How does the website function?
The ‘home’ page of the site should be modern, clean, and straight to the point (the
logos). The main focus is on the ‘logos’. There should be 5-6 logos per row and around
100 logos per page. The ‘description’ of each logo is NOT displayed UNTIL the visitor
clicks on a logo. Then the description, tags, category, and price will EXPAND ON SAME
PAGE (Not open in new page). Once the logo expands to reveal the description, tags,
category, and price, then the visitor can click on the name of the logo and THEN a
new page will open with options to add to cart or buy now.
What comes with each purchase?
1) Years of experience and expertise, ready to help builder your name!
2) Ownership of the valuable domain name, (digital real estate)
3) Custom logo artwork is included. And ideas for branding!
What happens after the customer completes purchase?
After completing our secure SSL checkout process, which accepts all major credit
cards and options for bank wire. The customer will be emailed transfer instructions.
The payment is held in escrow until the customer confirms delivery of the domain name.
Does title forge own all the names on the site?
Not all the names, some. title forge allows owners of domain names to
‘Submit’ their domain names for acceptance to be listed on our site. After our team ‘reviews’
the names, they will be accepted or rejected. The domain names that are suitable
for our target audience, will be emailed with instructions to ‘forward’ the domain to
the Title Forge site. Once our system verifies the domain is correctly forwarded, the
domain owner will be emailed with instructions and listing fees to be paid.
What the site needs:
1) The site must have a login for domain owners. Each domain owner will have
an account profile where they can:
• a) submit their domain names to list on our site
• b) verify accepted names
• c) pay listing fees
• d) describe what the domain means to the owner
• e) adjust the price (we determine fair market value) by 20% up or down.
• f) profile page (portfolio of names)
2) The site must display the logo artwork as the main focus of the site.
3) The site must have a newsletter page.
4) The site must have an about us page.
5) The site must have contact page.
6) The site must have a FAQ page.
7) The site must have a ‘search bar’
8) The site must have a ’price range filter’ to sort names.
9) The site must have an option to sort names by: categories
10) The site must have an option to ‘rearrange’ the logos by:
• a) ’Date’
• b) ’Price’
• c) ’Alphabetical order’
• d) ’Staff picks’.
Summary:
We want to help businesses build a name for their product/service/company. The true value of what we sell is in the domain names, however the inspiration, possibilities, and vision is captured in the logos. The site will get tons of natural traffic because all the domain names listed on the site will be forwarded to TitleForge.com and we will actively advertise. Upon arrival the visitors will see catchy, unique, and keyword rich logos. Upon clicking on a logo, the logo will expand to display, description, category, price, and possible business uses. Upon clicking further, a new page will open (the landing page for each domain name if entered directly into browser) which will give options to inquire, add to cart, favorite, or buy now!. There will be a login for domain owners where they can submit new domain names, verify ownership by forwarding domain, pay listing fee, describe accepted name, and adjust our chosen price up or down by 20%. They will also have a profile page which will display only their portfolio of names with logos. There will be a Newsletter, FAQ, About Us, Contact, and Login Pages.
Reason: Changed scope from coded to uncoded, and would like to see more designs before the deadline is up.
Target Market(s)
Business owners who want a brandable name for their business/service/product
Industry/Entity Type
Business
Number of Pages Required
1 page

```html
<!DOCTYPE html>
<html lang="en">
<head>
<meta charset="utf-8">
<title>TitleForge.com – Brandable Names</title>
<link rel="stylesheet" href="https://fonts.googleapis.com/css2?family=Raleway:wght@300;400;500&family=Roboto+Condensed:wght@400&family=Roboto:wght@400;700&family=Parisienne&display=swap">
<style>
:root{
  --purple:#6e64a9;
  --purple-text:#7d74c2;
  --footer-text:#d2cdee;
  --ink:#222;
  --muted:#666;
  --tile:#f2f2f2;
  --tile-line:#e4e4e4;
  --section:#f2f2f2;
  --band:#14191c;
  --green:#8cbd2c;
  --go:#a7c43c;
  --red:#c0302a;
}
*{box-sizing:border-box;margin:0;padding:0}
html,body{width:876px;height:1200px;overflow:hidden;background:#fff}
body{font-family:"Raleway",sans-serif;color:var(--ink)}
.page{position:relative;width:876px;height:1200px;overflow:hidden}
.abs{position:absolute}

/* top bar */
.topbar{left:0;top:0;width:876px;height:40px;background:#f4f4f4;border-bottom:1px solid #e2e2e2}
.social{left:452px;top:9px;display:flex;gap:5px}
.social span{width:20px;height:20px;border-radius:50%;background:#3a3a3a}
.social span.alt{background:#5b59b8}
.select{top:8px;height:24px;border:1px solid #dcdcdc;background:#fff;font-size:11px;color:#999;padding:5px 7px;font-family:"Raleway",sans-serif}
.select::after{content:"";position:absolute;right:0;top:0;width:18px;height:22px;background:#e4e4e4;border-left:1px solid #d6d6d6}
.select i{position:absolute;right:6px;top:10px;border:3px solid transparent;border-top-color:#888;z-index:1}
.select.category{left:586px;width:112px}
.select.sort{left:708px;width:94px}

/* header */
.brand{left:70px;top:78px;font-size:21px;font-weight:400;letter-spacing:.3px}
.brand small{font-size:14px}
.search{left:442px;top:83px;width:190px;height:25px;border:1px solid #d6d6d6}
.search svg{position:absolute;right:10px;top:6px}
.price-label{left:653px;top:67px;font-size:15px}
.slider{left:654px;top:91px;width:128px;height:3px;background:#e2e2e2}
.slider .fill{position:absolute;left:0;top:0;width:52px;height:3px;background:#111}
.slider .knob{position:absolute;top:-5px;width:10px;height:12px;background:#fff;border:1px solid #aaa;border-radius:2px 2px 6px 6px}
.price-min{left:655px;top:104px;font-size:11px}
.price-max{left:748px;top:104px;font-size:11px}

/* nav */
.nav{left:0;top:132px;width:876px;height:34px;background:var(--purple)}
.nav a{position:absolute;top:11px;color:#fff;text-decoration:none;font-family:"Roboto Condensed",sans-serif;font-size:10.5px}
.nav .divider{position:absolute;top:0;width:1px;height:34px;background:rgba(255,255,255,.25)}
.nav a.login{left:752px;top:9px;font-size:13.5px;font-family:"Raleway",sans-serif}

/* banner */
.banner{left:108px;top:192px;width:662px;height:98px;background:linear-gradient(#fff 0%,#f2f2f2 50%,#d4d4d4 100%)}
.banner h1{position:absolute;left:48px;top:18px;font-weight:400;font-size:34px;letter-spacing:.5px}
.banner .sub{position:absolute;right:338px;top:52px;color:var(--purple);font-size:21px;letter-spacing:.5px}
.banner .art{position:absolute;left:392px;top:10px;width:248px;height:72px;background:linear-gradient(100deg,#c9c9c9,#e8e8e8 60%,#b7b7b7);border-radius:4px}

/* grid */
.tile{width:101px;height:95px;background:var(--tile);border:1px solid var(--tile-line)}
.tile .mark{position:absolute;left:21px;top:18px;width:58px;height:58px}
.tile .mark.round{border-radius:50%}

.bubble{left:770px;top:558px;width:92px;height:48px;background:var(--green);border-radius:50%;color:#fff;font:9px/10px "Roboto",sans-serif;text-align:center;padding-top:9px}
.bubble::after{content:"";position:absolute;left:58px;top:42px;border:7px solid transparent;border-top:14px solid var(--green);transform:rotate(-25deg)}

/* support band */
.support{left:108px;top:646px;width:656px;height:64px;background:var(--band)}
.support p{position:absolute;left:0;top:15px;width:456px;text-align:center;color:#fff;font-size:15px;line-height:18px}
.support p span{color:var(--purple-text)}
.support .cta{position:absolute;left:471px;top:15px;width:136px;height:32px;background:var(--purple);color:#fff;font-size:17px;padding:4px 16px}

/* how it works */
.how{left:0;top:756px;width:876px;height:250px;background:var(--section)}
.video{left:82px;top:788px;width:256px;height:180px;background:#fff;box-shadow:0 6px 6px -3px rgba(0,0,0,.3)}
.video .photo{position:absolute;left:0;top:0;width:256px;height:180px;background:radial-gradient(ellipse 60px 95px at 50% 100%,#2b2c31 0%,#3c3d44 90%,#fff 92%)}
.video .bar{position:absolute;left:2px;bottom:6px;width:252px;height:12px;background:#2a2a2a;border-radius:2px}
.video .play{position:absolute;left:0;top:0;width:24px;height:12px;background:#444}
.video .play::after{content:"";position:absolute;left:9px;top:3px;border:3px solid transparent;border-left:5px solid #fff}
.video .track{position:absolute;left:28px;top:5px;width:160px;height:2px;background:#666}
.how h2{position:absolute;left:370px;top:26px;font-weight:400;font-size:21px}
.how .copy{position:absolute;left:370px;width:418px;font:10.4px/13.2px "Roboto",sans-serif;color:#333;text-align:justify}
.quote-mark{left:375px;top:917px;font:700 30px/30px Georgia,serif;color:var(--red)}
.promo{left:405px;top:938px;font:20px/22px "Parisienne",cursive;color:#555}
.promo span{display:block;padding-left:62px}

/* footer */
.footer{left:0;top:1006px;width:876px;height:194px;background:var(--purple)}
.footer h3{position:absolute;top:40px;font-weight:400;font-size:14px;color:#fff}
.footer .txt{position:absolute;font-size:10px;line-height:14.5px;color:var(--footer-text)}
.footer .link{color:#b5d334}
.footer b{color:#fff;font-family:"Roboto",sans-serif;font-weight:700}
.footer .icons{position:absolute;left:445px;top:157px;display:flex;gap:19px}
.footer .icons span{width:9px;height:9px;border-radius:50%;background:#fff}
.sub-input{position:absolute;left:630px;top:113px;width:126px;height:25px;background:#151515}
.sub-go{position:absolute;left:758px;top:113px;width:42px;height:25px;background:#151515;border:2px solid var(--go);color:#fff;font:700 9px/21px "Roboto",sans-serif;text-align:center}
</style>
</head>
<body>
<div class="page">

  <div class="abs topbar">
    <div class="abs social" aria-label="Social links">
      <span></span><span></span><span class="alt"></span><span></span><span></span>
    </div>
    <div class="abs select category">Category<i></i></div>
    <div class="abs select sort">Sort<i></i></div>
  </div>

  <div class="abs brand">TitleForge<small>.com</small></div>
  <div class="abs search">
    <svg width="13" height="13" viewBox="0 0 13 13"><circle cx="5.5" cy="5.5" r="4.2" fill="none" stroke="#222" stroke-width="1.8"/><line x1="8.5" y1="8.5" x2="12" y2="12" stroke="#222" stroke-width="2"/></svg>
  </div>
  <div class="abs price-label">Price</div>
  <div class="abs slider"><div class="fill"></div><div class="knob" style="left:47px"></div><div class="knob" style="left:120px"></div></div>
  <div class="abs price-min">$0.00</div>
  <div class="abs price-max">$600.00</div>

  <nav class="abs nav">
    <a style="left:73px">HOME</a><span class="divider" style="left:120px"></span>
    <a style="left:139px">SHOP</a><span class="divider" style="left:185px"></span>
    <a style="left:205px">HELP</a><span class="divider" style="left:250px"></span>
    <a style="left:269px">ABOUT</a><span class="divider" style="left:323px"></span>
    <a style="left:344px">NEWSLETTER</a>
    <a class="login">LOGIN</a>
  </nav>

  <section class="abs banner">
    <h1>Brandable names</h1>
    <div class="sub">invented</div>
    <div class="art" role="img" aria-label="3D grey lettering of a web address with a red question mark"></div>
  </section>

  <div class="abs tile" style="left:110px;top:314px"><div class="mark round" role="img" aria-label="Ship logo" style="background:#2f4858"></div></div>
  <div class="abs tile" style="left:221px;top:314px"><div class="mark round" role="img" aria-label="Green building leaf logo" style="background:#6fbf4a"></div></div>
  <div class="abs tile" style="left:330px;top:314px"><div class="mark" role="img" aria-label="Yellow arrow logo" style="background:#f3e01c"></div></div>
  <div class="abs tile" style="left:441px;top:314px"><div class="mark round" role="img" aria-label="Pink flame face logo" style="background:#e8428a"></div></div>
  <div class="abs tile" style="left:550px;top:314px"><div class="mark" role="img" aria-label="Embossed leaf and arrow logo" style="background:#9ea4a4"></div></div>
  <div class="abs tile" style="left:661px;top:314px"><div class="mark" role="img" aria-label="Sunrise chevron logo" style="background:linear-gradient(#f2a31c 40%,#1e4b70 41%)"></div></div>

  <div class="abs tile" style="left:110px;top:418px"><div class="mark round" role="img" aria-label="Home globe logo" style="background:#2aa98a"></div></div>
  <div class="abs tile" style="left:221px;top:418px"><div class="mark round" role="img" aria-label="Dental logo" style="background:#4cc3ea"></div></div>
  <div class="abs tile" style="left:330px;top:418px"><div class="mark round" role="img" aria-label="Hockey sticks emblem" style="background:#c9333c"></div></div>
  <div class="abs tile" style="left:441px;top:418px"><div class="mark" role="img" aria-label="Cloud chat logo" style="background:#3fb3e3"></div></div>
  <div class="abs tile" style="left:550px;top:418px"><div class="mark round" role="img" aria-label="Globe figure logo" style="background:#2f7fb5"></div></div>
  <div class="abs tile" style="left:661px;top:418px"><div class="mark round" role="img" aria-label="Eagle emblem" style="background:#5a4031"></div></div>

  <div class="abs tile" style="left:110px;top:524px"><div class="mark round" role="img" aria-label="Growth figure logo" style="background:#8fb02c"></div></div>
  <div class="abs tile" style="left:221px;top:524px"><div class="mark round" role="img" aria-label="Red robot logo" style="background:#e13a2e"></div></div>
  <div class="abs tile" style="left:330px;top:524px"><div class="mark" role="img" aria-label="Camera in a suit logo" style="background:#1e1e1e"></div></div>
  <div class="abs tile" style="left:441px;top:524px"><div class="mark" role="img" aria-label="Game chat logo" style="background:#f5e016"></div></div>
  <div class="abs tile" style="left:550px;top:524px"><div class="mark round" role="img" aria-label="Tree and spoon logo" style="background:#6eb43f"></div></div>
  <div class="abs tile" style="left:661px;top:524px"><div class="mark round" role="img" aria-label="Spider target logo" style="background:#1aa39a"></div></div>

  <div class="abs bubble">Didn't find the<br>name you wanted ?<br>CLICK here !</div>

  <section class="abs support">
    <p>Tired of subpar support? We're always available, and we're <span>empowered to help you.</span></p>
    <div class="cta">For Buyers</div>
  </section>

  <section class="abs how">
    <h2>How It Works !</h2>
    <p class="copy" style="top:60px">Lorem Ipsum is simply dummy text of the printing and typesetting industry. Lorem Ipsum has been the industry's standard dummy text ever since the 1500s, when an unknown printer took a galley of type and scrambled it to make a type specimen book. It has survived not only five centuries.</p>
    <p class="copy" style="top:124px">It was popularised in the 1960s with the release of Pressmark sheets containing Lorem Ipsum passages, and more recently with desktop publishing software like Quillset LayoutPro including versions of Lorem Ipsum.</p>
  </section>
  <div class="abs video">
    <div class="photo" role="img" aria-label="Support agent in a suit wearing a headset"></div>
    <div class="bar"><div class="play"></div><div class="track"></div></div>
  </div>
  <div class="abs quote-mark">&#8220;</div>
  <div class="abs promo">Your promotional text here Vivamus<span>volutpat ante, sit amet semper nisi</span></div>

  <footer class="abs footer">
    <h3 style="left:71px">About</h3>
    <p class="txt" style="left:71px;top:68px;width:165px">Lorem Ipsum is simply dummy text of the printing and typesetting industry. Lorem Ipsum has been the industry's standard dummy text ever since the 1500s, when an unknown printer took a galley.</p>

    <h3 style="left:258px">RSS Feeds</h3>
    <svg class="abs" style="left:258px;top:74px" width="9" height="9" viewBox="0 0 9 9"><circle cx="1.3" cy="7.7" r="1.3" fill="#fff"/><path d="M0 3.6a5.4 5.4 0 0 1 5.4 5.4M0 .8A8.2 8.2 0 0 1 8.2 9" fill="none" stroke="#fff" stroke-width="1.4"/></svg>
    <p class="txt" style="left:276px;top:70px">The Evolution Of Modern Retail<br><span class="link">http://lnk.to/7KqRtm2W</span></p>

    <h3 style="left:441px">Contact Info</h3>
    <p class="txt" style="left:440px;top:69px;width:176px;line-height:13px">48 Harbor Crest Ave, LA, CA 97845, US.</p>
    <p class="txt" style="left:440px;top:103px;font-size:11px;line-height:19px"><b>Phone:</b> +1 555 014 2290<br><b>Email:</b> &nbsp;info@titleforge.com</p>
    <div class="icons"><span></span><span></span><span></span><span></span><span></span></div>

    <h3 style="left:630px">Newsletter</h3>
    <p class="txt" style="left:630px;top:69px;width:180px;line-height:13px">Please, subscribe to our latest news to be upfated.</p>
    <div class="sub-input"></div>
    <div class="sub-go">GO</div>
  </footer>

</div>
</body>
</html>
```